Flyer-Design für online Buchverkaufsseite
Zielgruppe
Wir sind eine Onlien Ankaufsseite für Bücher.Wir kaufen Bücher zum Festpreis. Unsere Zielgruppe sind alle Haushalte, die ihre gebrauchten Bücher verkaufen wollen.
Aufgabenstellung
Nicht so viel Text reinpacken, alle wichtige Punkte sollen großer Schriftformat dargestellt werden.
Text soll vom Designer selbst erstellt werden.

```html
<!DOCTYPE html>
<html lang="de">
<head>
<meta charset="utf-8">
<title>buchflink.de – Flyer</title>
<link rel="stylesheet" href="https://fonts.googleapis.com/css2?family=Montserrat:wght@500;600;700&display=swap">
<style>
  :root{
    --stage:#d4d5d8;
    --paper:#ffffff;
    --ink:#111416;
    --brand:#3f6f86;
    --teal-dark:#1f4f5e;
    --teal-mid:#3f8796;
    --teal-light:#8fc9d2;
    --glow:#e9fbff;
    --shadow:rgba(0,0,0,.55);
  }
  *{margin:0;padding:0;box-sizing:border-box}
  html,body{width:1200px;height:675px;overflow:hidden}
  body{background:var(--stage);font-family:"Montserrat",sans-serif;position:relative}
  .flyer{position:absolute;top:4px;width:460px;height:651px;background:var(--paper);overflow:hidden;box-shadow:0 4px 10px rgba(0,0,0,.25)}
  .flyer--offer{left:89px}
  .flyer--contact{left:652px}
  .flyer__art{position:absolute;inset:0}
  .logo{position:absolute;top:14px;left:0;width:100%;display:flex;align-items:center;justify-content:center;gap:10px}
  .logo__dot{width:40px;height:40px;border-radius:50%;background:var(--brand)}
  .logo__name{font-weight:700;font-size:40px;color:var(--ink);letter-spacing:-.5px}
  .headline{position:absolute;left:15px;font-weight:600;line-height:1}
  .headline--question{top:432px;font-size:33px;color:var(--ink)}
  .headline--answer{top:470px;font-size:46px;color:#fff;text-shadow:0 0 2px var(--ink),1px 1px 0 var(--ink),-1px -1px 0 var(--ink),1px -1px 0 var(--ink),-1px 1px 0 var(--ink)}
  .claim{position:absolute;right:13px;top:528px;text-align:right;font-weight:500;font-size:15px;line-height:20px;color:#fff}
  .call{position:absolute;left:0;width:460px;text-align:center;color:#fff}
  .call__lead{top:576px;font-weight:500;font-size:18px;padding-left:2px}
  .call__main{top:600px;font-weight:600;font-size:37px;line-height:1}
  .welcome{position:absolute;left:15px;top:436px;font-weight:600;font-size:33px;line-height:41px;color:#f4fbfc;text-shadow:1px 2px 2px var(--shadow)}
  .contact{position:absolute;right:16px;top:546px;text-align:right;color:#fff;font-weight:500;font-size:15px;line-height:19.5px}
  .contact__title{font-weight:600;font-size:25px;line-height:30px;margin-bottom:2px}
</style>
</head>
<body>

<section class="flyer flyer--offer">
  <svg class="flyer__art" viewBox="0 0 460 651" width="460" height="651">
    <defs>
      <linearGradient id="booksTone" x1="0" y1="0" x2="1" y2="1">
        <stop offset="0" stop-color="#f2ece4"/>
        <stop offset=".35" stop-color="#c98f58"/>
        <stop offset=".6" stop-color="#e7c9a0"/>
        <stop offset="1" stop-color="#8c5a3a"/>
      </linearGradient>
      <linearGradient id="bookFade" x1="0" y1="0" x2="0" y2="1">
        <stop offset="0" stop-color="#fff" stop-opacity="1"/>
        <stop offset=".25" stop-color="#fff" stop-opacity="0"/>
      </linearGradient>
      <linearGradient id="womanTone" x1="0" y1="0" x2="1" y2="1">
        <stop offset="0" stop-color="#e8e6e6"/>
        <stop offset=".5" stop-color="#f3d6c6"/>
        <stop offset="1" stop-color="#4a5b68"/>
      </linearGradient>
      <linearGradient id="bandTone" x1="0" y1="0" x2="1" y2="1">
        <stop offset="0" stop-color="var(--teal-light)"/>
        <stop offset=".45" stop-color="var(--teal-mid)"/>
        <stop offset="1" stop-color="var(--teal-dark)"/>
      </linearGradient>
      <radialGradient id="sparkle" cx=".5" cy=".5" r=".5">
        <stop offset="0" stop-color="#fff" stop-opacity=".9"/>
        <stop offset="1" stop-color="#7fe3ff" stop-opacity="0"/>
      </radialGradient>
    </defs>
    <rect x="0" y="77" width="460" height="350" fill="url(#booksTone)" role="img" aria-label="Foto: Stapel gebrauchter Bücher mit einem aufgeschlagenen Buch im Vordergrund"/>
    <rect x="0" y="77" width="460" height="350" fill="url(#bookFade)"/>
    <circle cx="367" cy="296" r="94" fill="url(#womanTone)" stroke="var(--brand)" stroke-width="3" role="img" aria-label="Foto: Frau auf dem Sofa mit Laptop, lächelnd"/>
    <path d="M0,422 Q250,405 460,300 L460,651 L0,651 Z" fill="#fff"/>
    <path d="M0,426 Q250,410 460,306 L460,651 L0,651 Z" fill="url(#bandTone)"/>
    <path d="M0,586 Q330,505 460,314" fill="none" stroke="var(--glow)" stroke-width="3"/>
    <circle cx="20" cy="583" r="18" fill="url(#sparkle)"/>
    <circle cx="210" cy="517" r="22" fill="url(#sparkle)"/>
  </svg>

  <div class="logo">
    <span class="logo__dot"></span>
    <span class="logo__name">buchflink.de</span>
  </div>

  <p class="headline headline--question">Gebraucht?</p>
  <p class="headline headline--answer">Gekauft!</p>
  <p class="claim">Wir kaufen Deine gebrauchten<br>Bücher zum Festpreis.</p>
  <p class="call call__lead">Schnell, einfach und sicher.</p>
  <p class="call call__main">Schau vorbei!</p>
</section>

<section class="flyer flyer--contact">
  <svg class="flyer__art" viewBox="0 0 460 651" width="460" height="651">
    <defs>
      <linearGradient id="agentTone" x1="0" y1="0" x2="1" y2="0">
        <stop offset="0" stop-color="#dfe6ee"/>
        <stop offset=".35" stop-color="#b9a39a"/>
        <stop offset=".65" stop-color="#f1d3c4"/>
        <stop offset="1" stop-color="#e9e5e4"/>
      </linearGradient>
      <linearGradient id="bandTone2" x1="0" y1="0" x2="1" y2="1">
        <stop offset="0" stop-color="var(--teal-light)"/>
        <stop offset=".45" stop-color="var(--teal-mid)"/>
        <stop offset="1" stop-color="var(--teal-dark)"/>
      </linearGradient>
      <radialGradient id="sparkle2" cx=".5" cy=".5" r=".5">
        <stop offset="0" stop-color="#fff" stop-opacity=".9"/>
        <stop offset="1" stop-color="#7fe3ff" stop-opacity="0"/>
      </radialGradient>
    </defs>
    <rect x="0" y="0" width="460" height="430" fill="url(#agentTone)" role="img" aria-label="Foto: lächelnde Kundenberaterin mit Headset, Kolleginnen unscharf im Hintergrund"/>

    <g class="contact-icons" fill="#1e8fe0">
      <rect x="14" y="24" width="30" height="34" rx="2" fill="#f2f3f4"/>
      <rect x="20" y="35" width="18" height="13" fill="#1e8fe0"/>
      <path d="M20,35 L29,43 L38,35" fill="none" stroke="#fff" stroke-width="1.5"/>
      <rect x="46" y="22" width="30" height="36" rx="2" fill="#f2f3f4"/>
      <path d="M55,30 q-4,2 -1,12 q4,9 11,10 q3,0 3,-3 l-4,-4 q-2,2 -4,0 q-3,-4 -3,-8 q2,-1 1,-3 z"/>
      <rect x="78" y="24" width="30" height="36" rx="2" fill="#f2f3f4"/>
      <text x="93" y="48" font-family="Montserrat, sans-serif" font-weight="700" font-size="20" text-anchor="middle">@</text>
      <rect x="108" y="22" width="30" height="36" rx="2" fill="#f2f3f4"/>
      <rect x="116" y="28" width="14" height="25" rx="2"/>
      <rect x="118" y="31" width="10" height="9" fill="#f2f3f4"/>
      <rect x="140" y="24" width="30" height="36" rx="2" fill="#f2f3f4"/>
      <path d="M155,30 a7,7 0 0 1 7,7 c0,5 -7,13 -7,13 c0,0 -7,-8 -7,-13 a7,7 0 0 1 7,-7 z"/>
      <circle cx="155" cy="37" r="2.5" fill="#f2f3f4"/>
    </g>

    <path d="M0,422 Q280,410 460,300 L460,651 L0,651 Z" fill="#fff"/>
    <path d="M0,426 Q280,414 460,306 L460,651 L0,651 Z" fill="url(#bandTone2)"/>
    <path d="M0,586 Q330,505 460,314" fill="none" stroke="var(--glow)" stroke-width="3"/>
    <circle cx="10" cy="588" r="18" fill="url(#sparkle2)"/>
    <circle cx="218" cy="513" r="22" fill="url(#sparkle2)"/>
  </svg>

  <p class="welcome">Wir freuen uns<br>auf Dich.</p>
  <div class="contact">
    <p class="contact__title">Kontakt</p>
    <p>www.buchflink.de</p>
    <p>Lindenweg 12 | 38100 Musterstadt</p>
    <p>Telefon: 05 31 - 48 27 16 39 | Mail: info@buchflink.de</p>
  </div>
</section>

</body>
</html>
```